Website design to promote trampoline business

We require a website design for our business. The business is primarily provising access for people between 5YO and 40YO to jump on trampolines for fun and fitness.

We have a logo and color schemes already and the website should incorporate these colors and designs.

We would like to incorporate the following pages:-

Book Now!
Home
About Us
Locations & Hours
Jumping
Groups & Events
Gallery
Safety
Latest News
Careers

Industry/Entity Type

Business

Requirements
Must have
• Incorporate our logo and colors (files attached).

```html
<!DOCTYPE html>
<html lang="en">
<head>
<meta charset="utf-8">
<title>Sky Bounce Trampolines</title>
<link rel="stylesheet" href="https://fonts.googleapis.com/css2?family=Poppins:wght@400;500;600&family=Open+Sans:wght@400;600&display=swap">
<style>
:root{
  --orange:#f26a10;
  --brand-blue:#1b9ad8;
  --teal:#1ba4ae;
  --teal-dark:#15929b;
  --video-blue:#1e4f9b;
  --ink:#333;
  --muted:#555;
  --footer:#2b2b2b;
  --footer-deep:#1f1f1f;
  --white:#fff;
}
*{box-sizing:border-box;margin:0;padding:0}
html,body{width:1200px;height:3158px;overflow:hidden}
body{position:relative;font-family:"Open Sans",Arial,sans-serif;color:var(--ink);background:var(--white)}
.abs{position:absolute}
h2{font-family:"Poppins",Arial,sans-serif;font-weight:600}

/* header */
.topbar{left:0;top:0;width:1200px;height:100px;background:rgba(20,24,32,.72)}
.logo{left:132px;top:18px;font-family:"Poppins",Arial,sans-serif;font-weight:600;font-size:30px;line-height:1;color:var(--orange);display:flex;align-items:center;gap:10px}
.logo-mark{width:22px;height:22px;border-radius:50%;background:var(--brand-blue)}
.logo small{display:block}
.util-nav{right:132px;top:14px;display:flex;gap:30px;font-family:"Poppins",Arial,sans-serif;font-size:13px;color:var(--white)}
.main-nav{right:132px;top:62px;display:flex;gap:33px;font-family:"Poppins",Arial,sans-serif;font-size:15px;font-weight:500;color:var(--white)}

/* hero */
.hero{left:0;top:0;width:1200px;height:705px;background:linear-gradient(180deg,#6fa8d6 0%,#9cc4e2 35%,#4f6b4a 70%,#2f3a2a 100%)}
.hero-title{left:0;top:528px;width:1200px;text-align:center;font-family:"Poppins",Arial,sans-serif;font-weight:500;font-size:29px;line-height:38px;color:var(--white);text-shadow:0 2px 4px rgba(0,0,0,.5)}
.btn{display:flex;align-items:center;justify-content:center;background:var(--orange);color:var(--white);font-family:"Poppins",Arial,sans-serif;font-weight:500;border-radius:3px}
.hero-btn{left:506px;top:613px;width:188px;height:46px;font-size:20px}

/* welcome */
.section-title{font-size:22px}
.welcome-title{left:132px;top:772px;color:var(--brand-blue)}
.copy{font-size:12.5px;line-height:20px;color:var(--muted)}
.welcome-copy{left:132px;top:818px;width:530px}
.welcome-copy p+p{margin-top:18px}
.welcome-art{left:680px;top:725px;width:470px;height:400px;border-radius:8px;background:radial-gradient(ellipse at 60% 75%,#cfd8e6 0%,#e9eef5 45%,#ffffff 75%)}

/* video band */
.video{left:0;top:1132px;width:1200px;height:328px;background:linear-gradient(90deg,#1a4790 0%,#2a62b4 50%,#1d4f9b 100%)}
.video-title{left:132px;top:1183px;font-size:22px;color:var(--white)}
.play{left:130px;top:1244px}
.video-copy{left:684px;top:1322px;width:460px;font-size:16px;line-height:25px;color:var(--white)}

/* groups */
.groups-title{left:132px;top:1528px;color:#222}
.groups-copy{left:132px;top:1574px;width:455px}
.groups-btn{left:132px;top:1792px;width:152px;height:38px;font-size:16px}
.groups-art{left:671px;top:1540px;width:382px;height:316px;border-radius:6px;background:linear-gradient(135deg,#4a6fa8 0%,#6f9a5a 45%,#a9c08e 70%,#5a6e4a 100%)}

/* gallery & news */
.band{left:0;top:1908px;width:1200px;height:474px;background:var(--teal)}
.gallery-title{left:132px;top:1976px;color:var(--white)}
.gallery-rule{left:260px;top:1992px;width:490px;height:1px;background:rgba(255,255,255,.5)}
.gallery{left:132px;top:2026px;width:620px;display:grid;grid-template-columns:repeat(4,1fr);gap:8px}
.tile{height:135px}
.t1{background:linear-gradient(180deg,#6fb6e6,#c48a4a)}
.t2{background:linear-gradient(180deg,#4f7a4a,#9fbf8f)}
.t3{background:linear-gradient(180deg,#8cc4ec,#d8eaf6)}
.t4{background:linear-gradient(180deg,#f4f4f4,#ddd)}
.t5{background:linear-gradient(180deg,#5aa0dc,#cfe6f8)}
.t6{background:linear-gradient(180deg,#2e6fb4,#9bc7ea)}
.t7{background:linear-gradient(180deg,#6a8fb8,#dde6ee)}
.t8{background:linear-gradient(180deg,#4aa8e0,#e8d84a)}
.news-title{left:790px;top:1976px;color:var(--white)}
.news{left:790px;top:2026px;width:276px}
.news-item{padding-bottom:14px;margin-bottom:14px;border-bottom:1px solid rgba(255,255,255,.35)}
.news-item:last-child{border-bottom:0}
.news-date{font-size:11px;color:#e6f7f8}
.news-text{margin-top:6px;font-size:14px;line-height:20px;color:#0d3f5a;font-weight:600}

/* locations */
.locations{left:0;top:2382px;width:1200px;height:421px;background:radial-gradient(ellipse at 50% 50%,#f2f2f2 0%,#ffffff 70%)}
.loc-title{left:0;top:2446px;width:1200px;text-align:center;color:#222}
.loc-sub{left:0;top:2494px;width:1200px;text-align:center;font-size:12.5px;color:var(--muted)}
.hours{left:132px;top:2538px;width:236px;border-collapse:collapse;font-size:12.5px;color:var(--muted)}
.hours td{height:35px;border-bottom:1px solid #e2e2e2}
.hours td+td{text-align:right}
.field{background:#f3f3f3;border:1px solid #d6d6d6;border-radius:3px;font-size:12px;color:#666;padding:11px 10px}
.f-name{left:592px;top:2558px;width:232px;height:42px}
.f-email{left:592px;top:2608px;width:232px;height:42px}
.f-msg{left:837px;top:2558px;width:229px;height:92px;background:var(--white)}
.submit{left:592px;top:2663px;width:474px;height:40px;font-size:16px}

/* footer */
.footer{left:0;top:2803px;width:1200px;height:316px;background:var(--footer)}
.social{left:0;top:2857px;width:1200px;display:flex;justify-content:center;gap:26px}
.social span{width:22px;height:22px;border-radius:50%;background:#5a5a5a}
.social span.on{background:var(--brand-blue)}
.foot-title{left:0;top:2932px;width:1200px;text-align:center;font-size:20px;color:var(--white)}
.foot-copy{left:300px;top:2978px;width:600px;text-align:center;font-size:12px;line-height:20px;color:#ddd}
.foot-copy a{color:var(--brand-blue);text-decoration:none}
.foot-nav{left:0;top:3052px;width:1200px;display:flex;justify-content:center;gap:30px;font-size:13px;color:#ccc}
.copyright{left:0;top:3119px;width:1200px;height:39px;background:var(--footer-deep);display:flex;align-items:center;justify-content:center;font-size:12px;color:#aaa}
</style>
</head>
<body>

<div class="abs hero" role="img" aria-label="Photo of a child jumping on a backyard trampoline under a blue sky"></div>
<div class="abs topbar"></div>
<div class="abs logo"><span class="logo-mark"></span>Sky Bounce</div>
<nav class="abs util-nav"><span>Home</span><span>About Us</span><span>Book Now</span></nav>
<nav class="abs main-nav"><span>Locations &amp; Hours</span><span>Jumping</span><span>Groups &amp; Events</span><span>Gallery</span><span>Safety</span><span>News</span><span>Careers</span></nav>
<h1 class="abs hero-title">Lorem Ipsum is simply dummy text of the printing<br>and typesetting industry Lorem Ipsum.</h1>
<div class="abs btn hero-btn">Book Now!</div>

<h2 class="abs section-title welcome-title">Welcome to Sky Bounce Trampolines</h2>
<div class="abs copy welcome-copy">
  <p>Lorem ipsum is simply dummy text of the printing and typesetting industry. Lorem Ipsum has been the industry's standard dummy text ever since the 1500s, when an unknown printer took a galley of type and scrambled it to make a type specimen book.</p>
  <p>It has survived not only five centuries, but also the leap into electronic typesetting, remaining essentially unchanged. It was popularised in the 1960s with the release of printed sheets containing Lorem Ipsum passages, and more recently with desktop publishing software including versions of Lorem Ipsum. Contrary to popular belief, Lorem Ipsum is not simply random text. It has roots in a piece of classical Latin literature from 45 BC, making it over 2000 years old.</p>
</div>
<div class="abs welcome-art" role="img" aria-label="Three girls jumping above a round white and red trampoline"></div>

<div class="abs video" role="img" aria-label="Two kids leaping in the air against a blue backdrop"></div>
<h2 class="abs video-title">Watch Our Video</h2>
<svg class="abs play" width="92" height="92" viewBox="0 0 92 92" aria-hidden="true">
  <circle cx="46" cy="46" r="42" fill="none" stroke="#fff" stroke-width="5"/>
  <circle cx="46" cy="46" r="34" fill="#fff"/>
  <path d="M38 30 L62 46 L38 62 Z" fill="var(--video-blue)"/>
</svg>
<p class="abs video-copy">Lorem Ipsum is simply dummy text of the printing and typesetting industry. Lorem Ipsum has been the industry's standard dummy text.</p>

<h2 class="abs section-title groups-title">Groups &amp; Events</h2>
<p class="abs copy groups-copy">Lorem Ipsum is simply dummy text of the printing and typesetting industry. Lorem Ipsum has been the industry's standard dummy text ever since the 1500s, when an unknown printer took a galley of type and scrambled it to make a type specimen book. It has survived not only five centuries, but also the leap into electronic typesetting, remaining essentially unchanged. It was popularised in the 1960s with the release of sheets containing Lorem Ipsum passages, and more recently with desktop publishing software including versions of Lorem Ipsum.</p>
<div class="abs btn groups-btn">Click Here</div>
<div class="abs groups-art" role="img" aria-label="Fanned stack of photo panels showing groups of friends at events"></div>

<div class="abs band"></div>
<h2 class="abs section-title gallery-title">Our Gallery</h2>
<div class="abs gallery-rule"></div>
<div class="abs gallery">
  <div class="tile t1" role="img" aria-label="Athlete clearing a high jump bar"></div>
  <div class="tile t2" role="img" aria-label="Group of friends jumping outdoors"></div>
  <div class="tile t3" role="img" aria-label="Gymnast mid-flip in the air"></div>
  <div class="tile t4" role="img" aria-label="Person in a studio jump pose"></div>
  <div class="tile t5" role="img" aria-label="Woman jumping against the sky"></div>
  <div class="tile t6" role="img" aria-label="Two teens jumping together"></div>
  <div class="tile t7" role="img" aria-label="Dancer leaping on a beach"></div>
  <div class="tile t8" role="img" aria-label="Cheerleader jumping with pom poms"></div>
</div>
<h2 class="abs section-title news-title">Latest News</h2>
<div class="abs news">
  <div class="news-item"><div class="news-date">15 January 2014</div><div class="news-text">Lorem Ipsum is simply dummy text of the printing and typesetting industry Lorem Ipsum.</div></div>
  <div class="news-item"><div class="news-date">15 January 2014</div><div class="news-text">Lorem Ipsum is simply dummy text of the printing and typesetting industry Lorem Ipsum.</div></div>
  <div class="news-item"><div class="news-date">15 January 2014</div><div class="news-text">Lorem Ipsum is simply dummy text of the printing and typesetting industry Lorem Ipsum.</div></div>
</div>

<div class="abs locations"></div>
<h2 class="abs section-title loc-title">Locations &amp; Hours</h2>
<p class="abs loc-sub">Lorem Ipsum is simply dummy text of the printing and typesetting industry Lorem Ipsum has been the industry's.</p>
<table class="abs hours">
  <tr><td>Monday</td><td>8:00 AM - 5:00 PM</td></tr>
  <tr><td>Tuesday</td><td>8:00 AM - 5:00 PM</td></tr>
  <tr><td>Wednesday</td><td>8:00 AM - 5:00 PM</td></tr>
  <tr><td>Thursday</td><td>8:00 AM - 5:00 PM</td></tr>
  <tr><td>Friday</td><td>8:00 AM - 5:00 PM</td></tr>
  <tr><td>Saturday</td><td>8:00 AM - 5:00 PM</td></tr>
  <tr><td>Sunday</td><td>Closed</td></tr>
</table>
<div class="abs field f-name">Enter Your Name</div>
<div class="abs field f-email">Enter Your Email</div>
<div class="abs field f-msg">Enter Your Message</div>
<div class="abs btn submit">Submit Now</div>

<div class="abs footer"></div>
<div class="abs social" aria-label="Social links"><span></span><span class="on"></span><span></span><span></span><span></span></div>
<h2 class="abs foot-title">Contact us</h2>
<p class="abs foot-copy">Lorem ipsum dolor sit amet, consectetur <a>contact@skybouncepark.com</a> tellus mi, vel condimentum leo pharetra non. Nam et urna in tortor fermentum aliquam vel condimentum leo pharetra non Nam</p>
<nav class="abs foot-nav"><span>Home</span><span>About Us</span><span>Book Now</span><span>Locations &amp; Hours</span><span>Jumping</span><span>Groups &amp; Events</span><span>Gallery</span><span>Safety</span><span>News</span><span>Careers</span></nav>
<div class="abs copyright">Copyright © 2014 Sky Bounce Trampolines. All rights reserved.</div>

</body>
</html>
```